Grainwise Studio sell sheet

Make a 2 sided large format post card (5.5 x 8.5 inches) that introduces Grainwise Studio to prospective customers. Use the images and leave space for main selling points on front. Then leave space for a map and further details on the back.
PLEASE INCLUDE THE FOLLOWING CONTENT:
MAIN PAGE
heading:
Contract manufacturing & 3PL in Metro NYC
bullets:
Modern conveniently located facility with multiple lines. SQF, Kosher, Non-GMO, Organic, Gluten-Free.
Slabbing, single and coextrusion, baking, liquid & dry blending & filling.
3PL warehousing & fulfillment
BACK PAGE:
GrainWise Studio was created and is operated by experienced, successful natural food brand owners, as a higher-level contract manufacturing experience. Our goal is to provide the control and cost structure of self-manufacturing, while leveraging our capital investment and expertise.
You're always welcome to collaborate with us, observe your production and to enjoy our on-site fitness center, yoga classes, meditation, nursing and telework facilities.
Contact Mark Halloran 914-367-2041 mark@grainwise.example
Return address for postcard, should be small:
48 Birchfield Lane #317, Danbury CT 06811
Target Market(s)
B to B. We are an industrial contract manufacturer doing large volume production.
Industry/Entity Type
We design and manufacture natural food products for other companies to sell under their own brands.
Requirements
Must have
- Leave a small but adequate area for the postcard to be mailed. Must depict the some elements of all product stock images provided. Showing the full variety of food bars and product pouches and bottles we package so they are recognizable at a glance. The bar with the filling is not the major product, so even though it has it's own image, the other bars should be more prominent.
Nice to have
- A map same or similar to the one shown. The circle depicts the necessary visible radius. It can also be rectangular.

```html
<!DOCTYPE html>
<html lang="en">
<head>
<meta charset="utf-8">
<title>Grainwise Studio Postcard</title>
<link href="https://fonts.googleapis.com/css2?family=Bebas+Neue&family=Montserrat:wght@400;500&display=swap" rel="stylesheet">
<style>
  :root {
    --red: #e63a45;
    --coral: #e9464f;
    --orange: #f28a1c;
    --orange-dark: #c96a10;
    --ink: #262626;
    --paper: #ffffff;
    --stage: #ffffff;
    --grey-box: #ececec;
    --map-tone: #e4e6e1;
    --rule: #9a9a9a;
    --photo-dark: #5a4232;
    --photo-light: #c9a36f;
  }
  * { margin: 0; padding: 0; box-sizing: border-box; }
  html, body { width: 800px; height: 1200px; overflow: hidden; background: var(--stage); }
  .canvas { position: relative; width: 800px; height: 1200px; }
  .postcard {
    position: absolute; left: 38px; width: 725px; height: 484px;
    background: var(--paper); overflow: hidden;
    box-shadow: 0 4px 14px rgba(0,0,0,.22);
  }
  .postcard--front { top: 80px; }
  .postcard--back { top: 620px; }
  .postcard svg.shapes { position: absolute; inset: 0; }
  .display { font-family: "Bebas Neue", "Oswald", sans-serif; font-weight: 400; line-height: .9; position: absolute; white-space: nowrap; }
  .body-text { font-family: "Montserrat", Arial, sans-serif; position: absolute; }

  .brand { position: absolute; display: flex; align-items: center; gap: 8px; }
  .brand__dot { border-radius: 50%; background: var(--red); flex: none; }
  .brand__name { font-family: "Bebas Neue", sans-serif; color: var(--red); letter-spacing: .5px; white-space: nowrap; }

  /* Front */
  .front__brand { left: 40px; top: 50px; }
  .front__brand .brand__dot { width: 34px; height: 34px; }
  .front__brand .brand__name { font-size: 26px; }
  .title-main { left: 36px; top: 126px; font-size: 58px; color: var(--red); letter-spacing: -.5px; }
  .title-sub { left: 36px; top: 172px; font-size: 84px; color: var(--orange); }
  .title-rule { position: absolute; left: 38px; top: 244px; width: 22px; height: 2px; background: var(--rule); }
  .points-head { left: 37px; top: 258px; font-size: 17px; color: var(--red); }
  .points { position: absolute; left: 37px; top: 280px; width: 232px; list-style: none; }
  .points li {
    font-family: "Montserrat", sans-serif; font-size: 10px; line-height: 12.5px; color: var(--ink);
    position: relative; padding-left: 13px; margin-bottom: 5px;
  }
  .points li::before {
    content: ""; position: absolute; left: 0; top: 2.5px; width: 8px; height: 8px; border-radius: 50%;
    background: var(--orange); box-shadow: inset 0 0 0 2px #fbd2a3;
  }
  .call-front { left: 38px; top: 418px; font-size: 60px; color: var(--paper); }
  .badge-figure { left: 560px; top: 348px; font-size: 86px; color: var(--paper); width: 130px; text-align: center; }
  .badge-label { left: 560px; top: 430px; font-size: 34px; color: var(--ink); width: 130px; text-align: center; }

  /* Back */
  .back__heading { left: 38px; top: 30px; font-size: 17px; color: var(--paper); }
  .back__rule { position: absolute; left: 38px; top: 50px; width: 22px; height: 3px; background: var(--orange); }
  .back__copy { left: 40px; width: 281px; color: var(--paper); font-size: 9.4px; line-height: 12px; text-align: justify; }
  .back__copy--one { top: 64px; }
  .back__copy--two { top: 160px; }
  .back__map { position: absolute; left: 38px; top: 226px; width: 282px; height: 154px; border-radius: 16px; overflow: hidden; }
  .call-back { left: 38px; top: 412px; font-size: 34px; color: var(--paper); }
  .call-back span { color: var(--ink); }
  .back__contact { left: 40px; top: 452px; display: flex; gap: 16px; font-size: 9.6px; color: var(--paper); }
  .back__contact span { display: flex; align-items: center; gap: 4px; }
  .back__brand { left: 420px; top: 56px; }
  .back__brand .brand__dot { width: 18px; height: 18px; }
  .back__brand .brand__name { font-size: 15px; }
  .return-address { left: 421px; top: 80px; font-size: 8px; line-height: 11px; color: var(--ink); width: 160px; }
  .stamp { position: absolute; left: 601px; top: 33px; width: 93px; height: 93px; background: var(--grey-box); }
  .address-line { position: absolute; left: 441px; width: 253px; height: 1px; background: var(--rule); }
</style>
</head>
<body>
<main class="canvas">

  <section class="postcard postcard--front" aria-label="Postcard front">
    <svg class="shapes" width="725" height="484" viewBox="0 0 725 484">
      <defs>
        <clipPath id="hero-clip"><circle cx="660" cy="200" r="300"/></clipPath>
        <linearGradient id="bar-photo" x1="0" y1="0" x2="1" y2="1">
          <stop offset="0" stop-color="#5a4232"/>
          <stop offset=".55" stop-color="#c9a36f"/>
          <stop offset="1" stop-color="#8e3b2e"/>
        </linearGradient>
        <linearGradient id="bars-photo" x1="0" y1="0" x2="1" y2="0">
          <stop offset="0" stop-color="#d9b27a"/>
          <stop offset=".35" stop-color="#6a3b2a"/>
          <stop offset=".65" stop-color="#e0a245"/>
          <stop offset="1" stop-color="#b8643a"/>
        </linearGradient>
      </defs>
      <circle cx="660" cy="200" r="306" fill="none" stroke="var(--red)" stroke-width="6"/>
      <g role="img" aria-label="Photo of filled grain bars with strawberries">
        <rect x="0" y="0" width="725" height="484" fill="url(#bar-photo)" clip-path="url(#hero-clip)"/>
      </g>
      <circle cx="345" cy="185" r="32" fill="#f2a9d6"/>
      <circle cx="398" cy="160" r="36" fill="#9ccc48"/>
      <circle cx="305" cy="255" r="36" fill="#9ccc48"/>
      <circle cx="455" cy="222" r="44" fill="var(--orange)"/>
      <circle cx="375" cy="232" r="84" fill="var(--paper)"/>
      <g role="img" aria-label="Photo of assorted snack bars, pouches and bottles in rows">
        <circle cx="375" cy="232" r="78" fill="url(#bars-photo)"/>
      </g>
      <rect x="0" y="400" width="725" height="84" fill="var(--ink)"/>
      <path d="M508 484 Q530 300 725 300 L725 484 Z" fill="var(--orange)"/>
    </svg>

    <div class="brand front__brand"><span class="brand__dot"></span><span class="brand__name">Grainwise Studio</span></div>
    <h1 class="display title-main">GRAINWISE</h1>
    <p class="display title-sub">STUDIO</p>
    <span class="title-rule"></span>
    <h2 class="display points-head">Contract manufacturing &amp; 3PL in Metro NYC</h2>
    <ul class="points">
      <li>Modern conveniently located facility with multiple lines. SQF, Kosher, Non-GMO, Organic, Gluten-Free.</li>
      <li>Slabbing, single and coextrusion, baking, liquid &amp; dry blending &amp; filling.</li>
      <li>3PL warehousing &amp; fulfillment</li>
    </ul>
    <p class="display call-front">CALL US : 914-367-2041</p>
    <p class="display badge-figure">3PL</p>
    <p class="display badge-label">&amp; CO-PACKING</p>
  </section>

  <section class="postcard postcard--back" aria-label="Postcard back">
    <svg class="shapes" width="725" height="484" viewBox="0 0 725 484">
      <path d="M0 0 H342 A304 304 0 0 1 366 398 H0 Z" fill="var(--orange)"/>
      <g role="img" aria-label="Faint illustration of herbs, tomatoes and onions on red">
        <path d="M0 0 H334 A296 296 0 0 1 356 395 H0 Z" fill="var(--coral)"/>
      </g>
      <polygon points="335,395 362,395 362,370" fill="var(--orange-dark)"/>
      <rect x="0" y="395" width="362" height="89" fill="var(--orange)"/>
    </svg>

    <h2 class="display back__heading">ABOUT GRAINWISE STUDIO</h2>
    <span class="back__rule"></span>
    <p class="body-text back__copy back__copy--one">GrainWise Studio was created and is operated by experienced, successful natural food brand owners, as a higher-level contract manufacturing experience. Our goal is to provide the control and cost structure of self-manufacturing, while leveraging our capital investment and expertise.</p>
    <p class="body-text back__copy back__copy--two">You're always welcome to collaborate with us, observe your production and to enjoy our on-site fitness center, yoga classes, meditation, nursing and telework facilities.</p>
    <div class="back__map" role="img" aria-label="Map of Metro NYC showing the service radius around Danbury CT">
      <svg width="282" height="154" viewBox="0 0 282 154">
        <rect width="282" height="154" fill="var(--map-tone)"/>
      </svg>
    </div>
    <p class="display call-back">CALL MARK : <span>914-367-2041</span></p>
    <p class="body-text back__contact">
      <span>Contact Mark Halloran</span>
      <span><svg width="8" height="6" viewBox="0 0 8 6"><rect x=".5" y=".5" width="7" height="5" fill="none" stroke="#fff"/><path d="M.5 .5 L4 3.5 L7.5 .5" fill="none" stroke="#fff"/></svg>mark@grainwise.example</span>
    </p>

    <div class="brand back__brand"><span class="brand__dot"></span><span class="brand__name">Grainwise Studio</span></div>
    <p class="body-text return-address">48 Birchfield Lane #317<br>Danbury CT 06811</p>
    <div class="stamp"></div>
    <span class="address-line" style="top:262px"></span>
    <span class="address-line" style="top:298px"></span>
    <span class="address-line" style="top:335px"></span>
    <span class="address-line" style="top:371px"></span>
  </section>

</main>
</body>
</html>
```